Real Estate Seller Financing Postcard

I need a postcard that lays out these options contained in the notes that grabs attention, explains the two options easily and is eye-catching. The front needs to have the percentages on it and information about it and on the other side One side exact Text is:
"Monthly income without tenant headaches" in big letters. Also on front "Get
110%
add an "or"
160% of market value for your property. ". The percentages should be displayed and that is not to be a sentence of text. Other side text: I need bullets points for these "Formal protection as a lien holder against home
No commission or closing cost
Fast closings possible
Property taken as is so no repairs.

Add to the top of the back in "It’s simple. I am a new investor without down payment capital who still want to double our portfolio this year to grow our portfolio."
Here are the two options that are to be the largest part of the back
Option 1, you can receive 80% now cash and 30% over a short period of time including interest.

Option 2, where act like a bank allowing you to make 150% if you finance the whole property(ies). No gimmicks and surprises, just simple unconventional financing.

Include Logo Somewhere

Target Market(s)

Property Owners Wanting to Sell Their Property

Industry/Entity Type

Real Estate Investing

Requirements
Must have
• The options promiment and each side with its respective information. Must have logo somewhere
Nice to have
• The options in color other than black.
Should not have
• A picture of money on the front. Any other image is okay.

```html
<!DOCTYPE html>
<html lang="en">
<head>
<meta charset="utf-8">
<title>Meridian Real Estate Group – Seller Financing Postcard</title>
<link rel="stylesheet" href="https://fonts.googleapis.com/css2?family=Montserrat:wght@400;500;600;700;800;900&display=swap">
<style>
  :root {
    --stage: #cbcbcb;
    --paper: #ffffff;
    --indigo: #3b3897;
    --indigo-deep: #1d1a78;
    --navy: #16135e;
    --sky: #a9bede;
    --gold: #f5c416;
    --gold-deep: #e2a90b;
    --brand-blue: #2a5aa8;
    --grey-text: #6d6d6d;
    --ink: #1b1b4a;
  }
  * { box-sizing: border-box; margin: 0; padding: 0; }
  html, body { width: 1200px; height: 1177px; overflow: hidden; }
  body {
    background: var(--stage);
    font-family: "Montserrat", Arial, sans-serif;
    position: relative;
  }
  .card {
    position: absolute;
    left: 246px;
    width: 724px;
    height: 484px;
    background: var(--paper);
    overflow: hidden;
    box-shadow: 0 2px 6px rgba(0,0,0,0.12);
  }
  .card--front { top: 80px; }
  .card--back { top: 604px; }

  /* Brand mark */
  .brand {
    position: absolute;
    display: flex;
    align-items: center;
    gap: 12px;
  }
  .brand__dot {
    width: 62px; height: 62px;
    border-radius: 50%;
    border: 2px solid var(--brand-blue);
  }
  .brand__name {
    color: var(--brand-blue);
    font-weight: 500;
    font-size: 25px;
    line-height: 1.05;
    letter-spacing: 0.5px;
  }
  .brand__name small {
    display: block;
    font-size: 13px;
    letter-spacing: 0.3px;
  }

  /* FRONT */
  .headline {
    position: absolute;
    left: 22px; top: 18px;
    font-weight: 800;
    font-size: 37px;
    color: var(--indigo-deep);
    letter-spacing: 0.3px;
  }
  .headline-tag {
    position: absolute;
    left: 22px; top: 59px;
    width: 381px; height: 23px;
    background: var(--gold);
    color: var(--indigo-deep);
    font-weight: 700;
    font-size: 16.5px;
    text-align: center;
    line-height: 23px;
  }
  .front .brand { left: 452px; top: 20px; }

  .offer-band {
    position: absolute;
    left: 0; top: 102px;
    width: 724px; height: 270px;
    background: linear-gradient(90deg, var(--indigo) 0%, #5a58ae 35%, #8f9ccf 55%, var(--sky) 100%);
  }
  .offer-visual {
    position: absolute;
    left: 330px; top: 20px;
    width: 370px; height: 240px;
    background: radial-gradient(ellipse at 55% 60%, rgba(232,190,60,0.55) 0%, rgba(200,205,225,0.35) 55%, rgba(169,190,222,0) 80%);
  }
  .offer-get {
    position: absolute;
    left: 104px; top: 42px;
    font-weight: 800;
    font-size: 50px;
    color: #fff;
  }
  .rate {
    position: absolute;
    top: 96px;
    width: 108px; height: 108px;
    border-radius: 50%;
    background: radial-gradient(circle at 40% 35%, #fde37a 0%, var(--gold) 55%, var(--gold-deep) 100%);
    border: 5px solid #fff3b8;
    box-shadow: 0 0 0 3px var(--gold-deep);
    display: flex; align-items: center; justify-content: center;
    font-weight: 800;
    font-size: 27px;
    color: #fff;
    text-shadow: 0 1px 2px rgba(120,80,0,0.6);
  }
  .rate--1 { left: 11px; }
  .rate--2 { left: 124px; }
  .rate--3 { left: 241px; }
  .offer-note {
    position: absolute;
    left: 54px; top: 215px;
    font-weight: 600;
    font-size: 22px;
    color: #fff;
    letter-spacing: 0.5px;
  }
  .property-bar {
    position: absolute;
    left: 0; top: 372px;
    width: 724px; height: 47px;
    background: var(--gold);
  }
  .property-bar svg { position: absolute; left: 0; top: 0; }
  .property-bar__text {
    position: absolute;
    left: 0; right: 0; top: 0;
    text-align: center;
    line-height: 47px;
    font-weight: 700;
    font-size: 21px;
    letter-spacing: 7px;
    color: var(--navy);
  }
  .front-contact {
    position: absolute;
    left: 42px; top: 444px;
    font-size: 17px;
    font-weight: 500;
    color: var(--grey-text);
    letter-spacing: 0.5px;
  }
  .web-tab {
    position: absolute;
    left: 440px; top: 434px;
    width: 284px; height: 50px;
    background: var(--navy);
    clip-path: polygon(14px 0, 100% 0, 100% 100%, 0 100%);
    display: flex; align-items: center;
    padding-left: 28px; gap: 12px;
    color: #fff;
    font-weight: 700;
    font-size: 17.5px;
    letter-spacing: 0.6px;
    white-space: nowrap;
  }

  /* BACK */
  .back-shapes { position: absolute; left: 0; top: 0; }
  .back .brand { left: 448px; top: 14px; }
  .simple-title {
    position: absolute;
    left: 28px; top: 20px;
    font-weight: 800;
    font-size: 35px;
    color: #fff;
  }
  .simple-title em { font-style: normal; color: var(--gold); }
  .simple-intro {
    position: absolute;
    left: 28px; top: 74px;
    font-size: 14px;
    font-weight: 500;
    line-height: 1.2;
    letter-spacing: -0.2px;
    color: #fff;
    white-space: nowrap;
  }
  .simple-intro span { display: block; }
  .option {
    position: absolute;
    left: 20px;
    width: 376px;
    background: var(--gold);
    border-radius: 40px;
    display: flex; align-items: center;
  }
  .option--1 { top: 150px; height: 77px; }
  .option--2 { top: 243px; height: 79px; }
  .option__badge {
    flex: none;
    width: 68px; height: 68px;
    margin-left: 4px;
    border-radius: 50%;
    background: var(--indigo);
    border: 4px solid #fff;
    box-shadow: 0 0 0 2px var(--indigo);
    color: #fff;
    display: flex; flex-direction: column; align-items: center; justify-content: center;
    line-height: 1;
  }
  .option__badge small { font-size: 9px; font-weight: 700; letter-spacing: 0.5px; }
  .option__badge b { font-size: 26px; font-weight: 800; }
  .option__text {
    padding-left: 16px;
    padding-right: 14px;
    font-size: 12.6px;
    font-weight: 500;
    line-height: 1.28;
    color: var(--ink);
  }
  .option__text strong { font-weight: 800; }

  .benefits { position: absolute; left: 0; top: 346px; width: 470px; height: 138px; }
  .benefit {
    position: absolute;
    font-size: 12.5px;
    line-height: 1.25;
    color: var(--ink);
    text-transform: uppercase;
  }
  .benefit b { font-weight: 800; color: var(--indigo-deep); }
  .benefit--lien { left: 28px; top: 18px; }
  .benefit--fee { left: 270px; top: 20px; }
  .benefit--asis { left: 28px; top: 89px; }
  .benefit--fast { left: 270px; top: 89px; }
  .benefits svg { position: absolute; left: 0; top: 0; }

  .back-contact {
    position: absolute;
    left: 538px; top: 418px;
    width: 160px;
    text-align: center;
    font-size: 15.5px;
    font-weight: 500;
    line-height: 1.2;
    color: var(--navy);
  }
</style>
</head>
<body>

<section class="card card--front front" aria-label="Postcard front">
  <h1 class="headline">MONTHLY INCOME</h1>
  <div class="headline-tag">WITHOUT TENANT HEADACHES</div>
  <div class="brand">
    <span class="brand__dot"></span>
    <span class="brand__name">MERIDIAN<small>REAL ESTATE GROUP</small></span>
  </div>

  <div class="offer-band">
    <div class="offer-visual" role="img" aria-label="City skyline of tall buildings rising from stacks of gold coins"></div>
    <div class="offer-get">GET</div>
    <div class="rate rate--1">100%</div>
    <div class="rate rate--2">110%</div>
    <div class="rate rate--3">160%</div>
    <div class="offer-note">OF MARKET VALUE</div>
  </div>

  <div class="property-bar">
    <svg width="724" height="47" viewBox="0 0 724 47" aria-hidden="true">
      <polygon points="40,23.5 150,20.5 150,26.5" fill="#fff"/>
      <polygon points="684,23.5 574,20.5 574,26.5" fill="#fff"/>
    </svg>
    <div class="property-bar__text">FOR YOUR PROPERTY</div>
  </div>

  <div class="front-contact">COMPANY CONTACT</div>
  <div class="web-tab">
    <svg width="16" height="16" viewBox="0 0 16 16" aria-hidden="true">
      <g fill="none" stroke="#f5c416" stroke-width="1.4">
        <circle cx="8" cy="8" r="6.5"/>
        <ellipse cx="8" cy="8" rx="2.8" ry="6.5"/>
        <line x1="1.5" y1="8" x2="14.5" y2="8"/>
      </g>
    </svg>
    WWW.MERIDIAN.COM
  </div>
</section>

<section class="card card--back back" aria-label="Postcard back">
  <svg class="back-shapes" width="724" height="484" viewBox="0 0 724 484" aria-hidden="true">
    <defs>
      <linearGradient id="panelFill" x1="0" y1="0" x2="1" y2="1">
        <stop offset="0" stop-color="#5451ad"/>
        <stop offset="0.55" stop-color="#2f2b8c"/>
        <stop offset="1" stop-color="#1d1a78"/>
      </linearGradient>
    </defs>
    <polygon points="0,0 396,0 508,484 0,484" fill="#16135e"/>
    <polygon points="0,0 382,0 474,346 0,346" fill="url(#panelFill)"/>
    <polygon points="0,346 420,346 452,484 0,484" fill="#ffffff"/>
    <polygon points="484,380 724,380 724,484 514,484" fill="#f5c416"/>
  </svg>

  <div class="brand">
    <span class="brand__dot"></span>
    <span class="brand__name">MERIDIAN<small>REAL ESTATE GROUP</small></span>
  </div>

  <h2 class="simple-title">IT’S <em>SIMPLE</em> !</h2>
  <p class="simple-intro">
    <span>I am a new investor without down</span>
    <span>payment capital who still want to double</span>
    <span>our portfolio this year to grow our portfolio</span>
  </p>

  <div class="option option--1">
    <div class="option__badge"><small>OPTION</small><b>1</b></div>
    <p class="option__text">You can receive <strong>80%</strong> now cash and <strong>30%</strong> over a short period of time including interest.</p>
  </div>
  <div class="option option--2">
    <div class="option__badge"><small>OPTION</small><b>2</b></div>
    <p class="option__text">Where act like a bank allowing you to make <strong>150%</strong> if you finance the whole property(ies). No gimmicks &amp; surprises, just simple unconventional financing.</p>
  </div>

  <div class="benefits">
    <svg width="470" height="138" viewBox="0 0 470 138" aria-hidden="true">
      <line x1="22" y1="74" x2="410" y2="74" stroke="#3b3897" stroke-width="1.5"/>
      <line x1="215" y1="8" x2="215" y2="138" stroke="#3b3897" stroke-width="1.5"/>
      <circle cx="215" cy="74" r="34" fill="#fff" stroke="#16135e" stroke-width="4"/>
      <circle cx="215" cy="74" r="22" fill="#f5c416"/>
      <polyline points="205,74 213,82 227,64" fill="none" stroke="#16135e" stroke-width="4" stroke-linecap="round" stroke-linejoin="round"/>
    </svg>
    <p class="benefit benefit--lien"><b>Formal protection</b><br>as a lien holder<br>against home</p>
    <p class="benefit benefit--fee"><b>No commission</b><br>or closing cost</p>
    <p class="benefit benefit--asis">Property taken<br>as is so <b>no repairs</b></p>
    <p class="benefit benefit--fast"><b>Fast closings</b><br>possible</p>
  </div>

  <div class="back-contact">COMPANY<br>CONTACT</div>
</section>

</body>
</html>
```